Hotel Business Card Project

Amber Crest Hotel will be a premium boutique hotel in Dhaka, Bangladesh. The hotel will offer the finest amenities and facilities available on the market, and the cost per room investment will far exceed other 5-star hotels currently in the market.

As a result, we wanted the business card to reflect that premium/luxurious/upscale feel, and also be elegant and hospitable at the same time.

The name 'Amber Crest' is derived from the fact that Bangladesh has 6 distinct seasons (you can get more information online if required, or contact me about it). The leaves in the logo has the tree because trees give people shade, protection and safety (just like our hotel would try to give).

Target Market(s)

Business professionals, guests

Industry/Entity Type

Investment

Requirements
Must have
• Elegant, Classy and very attractive business card.

Must be editable to enter specific Names, Positions, Phone numbers and email later on.
Nice to have
• The address would be: House 42, Road 57, Banani 4, Dhaka 1230, Bangladesh

Slogan- Luxury Redefined

```html
<!DOCTYPE html>
<html lang="en">
<head>
<meta charset="utf-8">
<title>Amber Crest Hotel – Business Card</title>
<link rel="stylesheet" href="https://fonts.googleapis.com/css2?family=Montserrat:wght@300;400&display=swap">
<style>
  :root {
    --backdrop: #e9e6e2;
    --card-white: #ffffff;
    --brand-brown: #3d2b20;
    --slogan-grey: #9a9a9a;
    --rule-grey: #c9c9c9;
    --green-light: #b2d61a;
    --green-mid: #95c414;
    --green-deep: #6c9f10;
    --text-on-green: #ffffff;
    --shadow: rgba(40, 25, 15, 0.22);
  }
  html, body {
    margin: 0;
    padding: 0;
    overflow: hidden;
  }
  body {
    width: 1200px;
    height: 861px;
    background: var(--backdrop);
    font-family: "Montserrat", sans-serif;
    position: relative;
  }
  .card {
    position: absolute;
    top: 288px;
    width: 500px;
    height: 286px;
    box-shadow: 0 10px 28px var(--shadow);
    overflow: hidden;
  }
  /* Front */
  .card--front {
    left: 70px;
    background: var(--card-white);
    display: flex;
    flex-direction: column;
    align-items: center;
    justify-content: center;
  }
  .brand-mark {
    display: flex;
    align-items: center;
    gap: 12px;
  }
  .brand-mark__dot {
    width: 14px;
    height: 14px;
    border-radius: 50%;
    background: var(--brand-brown);
  }
  .brand-name {
    font-weight: 400;
    font-size: 27px;
    letter-spacing: 2px;
    text-transform: uppercase;
    color: var(--brand-brown);
    margin: 0;
  }
  .front-rule {
    width: 200px;
    height: 1px;
    background: var(--rule-grey);
    margin: 18px 0 14px;
  }
  .slogan {
    font-weight: 300;
    font-size: 13px;
    letter-spacing: 4px;
    text-transform: uppercase;
    color: var(--slogan-grey);
    margin: 0;
  }
  /* Back */
  .card--back {
    left: 630px;
    background: radial-gradient(ellipse at 72% 40%, var(--green-light) 0%, var(--green-mid) 55%, var(--green-deep) 100%);
  }
  .back-glow {
    position: absolute;
    right: -40px;
    top: 10px;
    width: 300px;
    height: 300px;
  }
  .back-layout {
    position: relative;
    display: flex;
    align-items: center;
    height: 100%;
    padding: 0 26px;
    box-sizing: border-box;
  }
  .back-brand {
    display: flex;
    align-items: center;
    gap: 8px;
    width: 140px;
  }
  .back-brand__dot {
    width: 9px;
    height: 9px;
    border-radius: 50%;
    background: var(--text-on-green);
    flex: none;
  }
  .back-brand__name {
    font-weight: 400;
    font-size: 14px;
    letter-spacing: 1px;
    text-transform: uppercase;
    color: var(--text-on-green);
    margin: 0;
    line-height: 1.25;
  }
  .back-divider {
    width: 1px;
    height: 96px;
    background: rgba(255, 255, 255, 0.75);
    margin: 0 18px 0 8px;
  }
  .contact {
    list-style: none;
    margin: 0;
    padding: 0;
    color: var(--text-on-green);
    font-weight: 400;
    font-size: 9.5px;
    line-height: 1.55;
  }
</style>
</head>
<body>
  <section class="card card--front" aria-label="Card front">
    <div class="brand-mark">
      <span class="brand-mark__dot"></span>
      <h1 class="brand-name">Amber Crest Hotel</h1>
    </div>
    <div class="front-rule"></div>
    <p class="slogan">Luxury Redefined</p>
  </section>

  <section class="card card--back" aria-label="Card back">
    <svg class="back-glow" viewBox="0 0 300 300" aria-hidden="true">
      <circle cx="150" cy="150" r="140" fill="#ffffff" fill-opacity="0.08"/>
    </svg>
    <div class="back-layout">
      <div class="back-brand">
        <span class="back-brand__dot"></span>
        <p class="back-brand__name">Amber Crest Hotel</p>
      </div>
      <div class="back-divider"></div>
      <ul class="contact">
        <li>House 42, Road 57, Banani 4, Dhaka 1230, Bangladesh</li>
        <li>P: 000.000.0000</li>
        <li>EMAIL: nadia@ambercresthotel.com</li>
        <li>ambercresthotel.com</li>
      </ul>
    </div>
  </section>
</body>
</html>
```